Medical Device - Case Study Template

We need a TEMPLATE that we can reuse to write various case studies about the medical equipment solutions we provide. It will be a double sided letter sized with a modern design that conveys a feeling of expertise, innovation and highly personable service AND be consistent with the brand guide. The content will be divided into a few sections:

- Situation (200-250 words)
- Challenge (100-120 words)
- Solution (100-120 words)
- Results (100-120 words)
- Conclusion (100-120 words)

Additionally, there will need to be a call to action, inviting people to send an email for more information and a short "About Valtu" section (approx. 40 words).

For device picture placeholders, feel free to use any random small benchtop medical device.

```html
<!DOCTYPE html>
<html lang="en">
<head>
<meta charset="utf-8">
<title>Valtu – Case Study Template</title>
<link href="https://fonts.googleapis.com/css2?family=Lexend:wght@300;400;500;600;700&display=swap" rel="stylesheet">
<style>
  :root{
    --navy:#1b2a5c;
    --orange:#e8531f;
    --heading:#1d5aa8;
    --about:#6596cc;
    --brand-blue:#4a6d96;
    --body:#3a3a3a;
    --paper:#ffffff;
    --stage:#e2e2e2;
    --rule:#5d84c0;
    --edge:#4f78b4;
  }
  *{box-sizing:border-box;margin:0;padding:0}
  html,body{width:984px;height:1200px;overflow:hidden;background:var(--stage)}
  body{position:relative;font-family:"Lexend",sans-serif;color:var(--body)}

  .page{position:absolute;top:299px;width:727px;height:960px;background:var(--paper);
        transform:scale(0.6272);transform-origin:top left;overflow:hidden;
        box-shadow:0 10px 24px rgba(0,0,0,.25)}
  .page--front{left:24px}
  .page--back{left:504px}

  /* brand */
  .brand{position:absolute;white-space:nowrap}
  .brand__row{display:flex;align-items:center;gap:14px}
  .brand__dot{width:40px;height:40px;border-radius:50%;background:var(--orange)}
  .brand__name{font-size:48px;font-weight:400;color:var(--brand-blue);line-height:1;letter-spacing:1px}
  .brand__tagline{display:block;font-size:16px;font-weight:300;color:var(--brand-blue);letter-spacing:1.5px;margin:6px 0 0 70px}

  /* front hero */
  .hero{position:absolute;left:0;top:115px;width:727px;height:372px;background:var(--navy)}
  .hero__rule{position:absolute;left:0;top:180px;width:727px;height:4px;background:#fff}
  .hero__kicker{position:absolute;left:27px;top:40px;font-size:44px;font-weight:600;color:var(--about);line-height:1}
  .hero__title{position:absolute;left:25px;top:86px;font-size:64px;font-weight:700;color:#fff;line-height:1;letter-spacing:1px}
  .hero__photo{position:absolute;left:0;top:0}
  .hero__intro{position:absolute;left:27px;top:196px;width:420px;height:160px}
  .hero__wrap{float:right;width:420px;height:160px;
              shape-outside:polygon(286px 0,420px 0,420px 160px,404px 160px)}
  .hero__intro p{font-size:14.2px;font-weight:500;color:#fff;line-height:18px;text-align:justify}

  /* sections */
  .section{position:absolute;left:30px;width:670px}
  .section__head{display:block;margin-bottom:14px;white-space:nowrap}
  .section__icon{display:inline-block;width:22px;height:22px;vertical-align:-3px;margin-right:8px}
  .section__title{display:inline;font-size:22px;font-weight:600;color:var(--heading);letter-spacing:.3px}
  .section p{font-size:11.4px;line-height:13.4px;text-align:justify;margin-bottom:13px;font-weight:300;color:var(--body)}

  /* back: text flowing beside the photo */
  .flow{position:absolute;left:30px;top:40px;width:500px;height:390px}
  .flow__wrap{float:right;width:500px;height:390px;
              shape-outside:polygon(440px 0,500px 0,500px 390px,486px 390px,346px 142px)}
  .flow .block{position:static;width:auto}
  .flow .block--results{margin-top:18px}

  /* footer */
  .footer{position:absolute;left:0;bottom:0;width:727px;height:62px;background:var(--navy);
          display:flex;align-items:center;gap:30px;padding-left:50px}
  .footer__item{display:flex;align-items:center;gap:10px;color:#fff;font-size:15px;letter-spacing:1.8px;font-weight:400;white-space:nowrap}
  .footer__icon{width:20px;height:18px}
  .page-edge{position:absolute;right:0;bottom:0}

  /* back */
  .back__bar{position:absolute;left:0;top:0}
  .back__line{position:absolute;left:18px;top:10px;width:2px;height:680px;background:var(--rule)}
  .back__photo{position:absolute;left:0;top:0}
  .cta{position:absolute;left:18px;top:700px}
  .cta__accent{position:absolute;left:0;top:0;width:4px;height:88px;background:var(--orange)}
  .cta__title{position:absolute;left:26px;top:110px;white-space:nowrap;font-size:22px;font-weight:600;color:var(--heading)}
  .cta__sub{position:absolute;left:26px;top:137px;white-space:nowrap;font-size:19px;font-weight:500;color:var(--orange)}
  .cta__phone{position:absolute;left:26px;top:165px;white-space:nowrap;display:flex;align-items:center;gap:8px;font-size:20px;font-weight:500;color:var(--heading);letter-spacing:2px}
  .device{position:absolute;left:462px;top:700px}
</style>
</head>
<body>

<section class="page page--front">
  <div class="brand" style="left:228px;top:28px">
    <div class="brand__row"><span class="brand__dot"></span><span class="brand__name">Valtu</span></div>
    <span class="brand__tagline">Medical Technology</span>
  </div>

  <div class="hero">
    <div class="hero__rule"></div>
    <div class="hero__kicker">ABOUT</div>
    <div class="hero__title">VALTU</div>
    <svg class="hero__photo" width="727" height="372" viewBox="0 0 727 372">
      <defs>
        <linearGradient id="surgeonTone" x1="0" y1="0" x2="1" y2="1">
          <stop offset="0" stop-color="#2b3f66"/>
          <stop offset=".5" stop-color="#3e7ea6"/>
          <stop offset="1" stop-color="#1d4e72"/>
        </linearGradient>
      </defs>
      <polygon role="img" aria-label="Photo of a doctor wearing a VR headset working with a holographic medical interface"
        points="316,182 440,27 610,27 702,182 610,343 440,343"
        fill="url(#surgeonTone)" stroke="var(--orange)" stroke-width="3"/>
    </svg>
    <div class="hero__intro">
      <div class="hero__wrap"></div>
      <p>Lorem Ipsum is simply dummy text of the printing and typesetting industry. Lorem Ipsum has been the industry's standard dummy text ever since the 1500s, when an unknown printer took a galley of type and scrambled it to make a type specimen book.</p>
    </div>
  </div>

  <div class="section" style="top:515px">
    <div class="section__head">
      <svg class="section__icon" viewBox="0 0 22 22" fill="none" stroke="var(--orange)" stroke-width="1.6"><rect x="3" y="2" width="13" height="17" rx="1.5"/><line x1="6" y1="7" x2="13" y2="7"/><line x1="6" y1="11" x2="11" y2="11"/><circle cx="15" cy="15" r="3.5"/><line x1="17.5" y1="17.5" x2="20.5" y2="20.5"/></svg><h2 class="section__title">SITUATION</h2>
    </div>
    <p>Lorem Ipsum is simply dummy text of the printing and typesetting industry. Lorem Ipsum has been the industry's standard dummy text ever since the 1500s, when an unknown printer took a galley of type and scrambled it to make a type specimen book. It has survived not only five centuries, but also the leap into electronic typesetting, remaining essentially unchanged. It was popularised in the 1960s with the release of Typeset sheets containing Lorem Ipsum passages, and more recently with desktop publishing software like Folio Layout including versions of Lorem Ipsum.</p>
    <p>Lorem Ipsum is simply dummy text of the printing and typesetting industry. Lorem Ipsum has been the industry's standard dummy text ever since the 1500s, when an unknown printer took a galley of type and scrambled it to make a type specimen book.</p>
  </div>

  <div class="section" style="top:702px">
    <div class="section__head">
      <svg class="section__icon" viewBox="0 0 22 22" fill="none" stroke="var(--orange)" stroke-width="1.6"><rect x="2" y="7" width="18" height="13" rx="1.5"/><path d="M5 7 L11 2 L17 7"/><circle cx="11" cy="13.5" r="3"/></svg><h2 class="section__title">CHALLENGE</h2>
    </div>
    <p>Lorem Ipsum is simply dummy text of the printing and typesetting industry. Lorem Ipsum has been the industry's standard dummy text ever since the 1500s, when an unknown printer took a galley of type and scrambled it to make a type specimen book. It has survived not only five centuries, but also the leap into electronic typesetting, remaining essentially unchanged. It was popularised in the 1960s with the release of Typeset sheets containing Lorem Ipsum passages, and more recently with desktop publishing software like Folio Layout including versions of Lorem Ipsum.</p>
    <p>Lorem Ipsum is simply dummy text of the printing and typesetting industry. Lorem Ipsum has been the industry's standard dummy text ever since the 1500s, when an unknown printer took a galley of type and scrambled it to make a type specimen book.</p>
  </div>

  <svg class="page-edge" width="727" height="110" viewBox="0 0 727 110">
    <polygon points="0,104 0,98 700,98 727,52 727,104" fill="var(--edge)"/>
    <polygon points="0,110 0,101 695,101 727,58 727,110" fill="var(--navy)"/>
  </svg>
  <footer class="footer">
    <span class="footer__item"><svg class="footer__icon" viewBox="0 0 20 18"><rect x="1" y="3" width="18" height="12" fill="var(--orange)"/><path d="M1 3 L10 10 L19 3" fill="none" stroke="var(--navy)" stroke-width="1.5"/></svg>email ID address</span>
    <span class="footer__item"><svg class="footer__icon" viewBox="0 0 20 18" fill="none" stroke="var(--orange)" stroke-width="1.6"><circle cx="10" cy="9" r="7.5"/><ellipse cx="10" cy="9" rx="3.2" ry="7.5"/><line x1="2.5" y1="9" x2="17.5" y2="9"/></svg>website address</span>
    <span class="footer__item"><svg class="footer__icon" viewBox="0 0 20 18"><path d="M5 1 L8 5 L6 7 Q8 11 11 13 L13 11 L17 14 L15 17 Q5 15 3 3 Z" fill="var(--orange)"/></svg>0000 000 000</span>
  </footer>
</section>

<section class="page page--back">
  <svg class="back__bar" width="727" height="12" viewBox="0 0 727 12"><polygon points="0,0 527,0 520,10 0,10" fill="var(--orange)"/></svg>
  <div class="back__line"></div>
  <svg class="back__photo" width="727" height="420" viewBox="0 0 727 420">
    <defs>
      <linearGradient id="xrayTone" x1="0" y1="0" x2="1" y2="1">
        <stop offset="0" stop-color="#1e2a3e"/>
        <stop offset=".45" stop-color="#6c7e96"/>
        <stop offset="1" stop-color="#e6ecf4"/>
      </linearGradient>
    </defs>
    <polygon role="img" aria-label="Photo of a tablet showing chest X-ray images on a desk"
      points="521,0 727,0 727,410 533,410 401,182" fill="url(#xrayTone)"/>
    <polyline points="521,0 401,182 533,410 727,410" fill="none" stroke="var(--orange)" stroke-width="3"/>
  </svg>

  <div class="flow">
    <div class="flow__wrap"></div>
    <div class="section block">
      <div class="section__head">
        <svg class="section__icon" viewBox="0 0 22 22" fill="none" stroke="var(--orange)" stroke-width="1.6"><circle cx="11" cy="8" r="5.5"/><path d="M8 13 L8 17 L14 17 L14 13"/><line x1="9" y1="20" x2="13" y2="20"/></svg><h2 class="section__title">SOLUTION</h2>
      </div>
      <p>Lorem Ipsum is simply dummy text of the printing and typesetting industry. Lorem Ipsum has been the industry's standard dummy text ever since the 1500s, when an unknown printer took a galley of type and scrambled it to make a type specimen book. It has survived not only five centuries, but also the leap into electronic typesetting, remaining essentially unchanged. It was popularised in the 1960s with the release of Typeset sheets containing Lorem Ipsum passages, and more recently with desktop publishing software like Folio Layout including versions of Lorem Ipsum.</p>
      <p>Lorem Ipsum is simply dummy text of the printing and typesetting industry.</p>
    </div>
    <div class="section block block--results">
      <div class="section__head">
        <svg class="section__icon" viewBox="0 0 22 22" fill="none" stroke="var(--orange)" stroke-width="1.6"><rect x="2" y="3" width="18" height="16" rx="1.5"/><polyline points="5,15 9,10 12,13 17,7"/></svg><h2 class="section__title">RESULTS</h2>
      </div>
      <p>Lorem Ipsum is simply dummy text of the printing and typesetting industry. Lorem Ipsum has been the industry's standard dummy text ever since the 1500s, when an unknown printer took a galley of type and scrambled it to make a type specimen book. It has survived not only five centuries, but also the leap into electronic typesetting, remaining essentially unchanged. It was popularised in the 1960s with the release of Typeset sheets containing Lorem Ipsum passages, and more recently with desktop publishing software like Folio Layout including versions of Lorem Ipsum.</p>
    </div>
  </div>

  <div class="section" style="top:440px">
    <div class="section__head">
      <svg class="section__icon" viewBox="0 0 22 22" fill="none" stroke="var(--orange)" stroke-width="1.6"><circle cx="11" cy="8" r="5.5"/><path d="M8 13 L8 17 L14 17 L14 13"/><line x1="9" y1="20" x2="13" y2="20"/></svg><h2 class="section__title">CONCLUSION</h2>
    </div>
    <p>Lorem Ipsum is simply dummy text of the printing and typesetting industry. Lorem Ipsum has been the industry's standard dummy text ever since the 1500s, when an unknown printer took a galley of type and scrambled it to make a type specimen book. It has survived not only five centuries, but also the leap into electronic typesetting, remaining essentially unchanged. It was popularised in the 1960s with the release of Typeset sheets containing Lorem Ipsum passages, and more recently with desktop publishing software like Folio Layout including versions of Lorem Ipsum.</p>
    <p>Lorem Ipsum is simply dummy text of the printing and typesetting industry. Lorem Ipsum has been the industry's standard dummy text ever since the 1500s, when an unknown printer took a galley of type and scrambled it to make a type specimen book.</p>
    <p>Contrary to popular belief, Lorem Ipsum is not simply random text. It has roots in a piece of classical Latin literature from 45 BC, making it over 2000 years old. Henry Dallow, a Latin professor at Ashford Hill College in Vermont, looked up one of the more obscure Latin words, consectetur, from a Lorem Ipsum passage</p>
  </div>

  <div class="cta">
    <div class="cta__accent"></div>
    <div class="brand" style="left:26px;top:8px">
      <div class="brand__row"><span class="brand__dot"></span><span class="brand__name">Valtu</span></div>
      <span class="brand__tagline">Medical Technology</span>
    </div>
    <div class="cta__title">CALL TO ACTION</div>
    <div class="cta__sub">Send an email for more information</div>
    <div class="cta__phone"><svg width="18" height="20" viewBox="0 0 20 18"><path d="M5 1 L8 5 L6 7 Q8 11 11 13 L13 11 L17 14 L15 17 Q5 15 3 3 Z" fill="var(--orange)"/></svg>0000 000 000</div>
  </div>

  <svg class="page-edge" width="727" height="110" viewBox="0 0 727 110">
    <polygon points="0,104 0,98 700,98 727,52 727,104" fill="var(--edge)"/>
    <polygon points="0,110 0,101 695,101 727,58 727,110" fill="var(--navy)"/>
  </svg>
  <footer class="footer">
    <span class="footer__item"><svg class="footer__icon" viewBox="0 0 20 18"><rect x="1" y="3" width="18" height="12" fill="var(--orange)"/><path d="M1 3 L10 10 L19 3" fill="none" stroke="var(--navy)" stroke-width="1.5"/></svg>email ID address</span>
    <span class="footer__item"><svg class="footer__icon" viewBox="0 0 20 18" fill="none" stroke="var(--orange)" stroke-width="1.6"><circle cx="10" cy="9" r="7.5"/><ellipse cx="10" cy="9" rx="3.2" ry="7.5"/><line x1="2.5" y1="9" x2="17.5" y2="9"/></svg>website address</span>
  </footer>

  <svg class="device" width="230" height="260" viewBox="0 0 230 260">
    <defs>
      <linearGradient id="deviceTone" x1="0" y1="0" x2="0" y2="1">
        <stop offset="0" stop-color="#f4f5f7"/>
        <stop offset="1" stop-color="#cfd4dc"/>
      </linearGradient>
    </defs>
    <rect role="img" aria-label="Photo of a white benchtop clinical chemistry analyzer with an open lid"
      x="8" y="4" width="214" height="250" rx="14" fill="url(#deviceTone)"/>
  </svg>
</section>

</body>
</html>
```